Business card for technical support company.
FixWiseDesk.com
Business card for technical support company.  - Computers
Creative Brief
Use specific fonts
Up To designer
Professional
Marcus Bell
VP In Charge
482 Alder Lane New York, NY 48213
service@FixWiseDesk.com
This will be used as a mock-up for my business card. Editable Adobe Illustrator or comparable original design file will need to be included with the final design. Also logo can be broken up from the FixWiseDesk.com below it and arranged on the card.
Company logo, website, and possible list of services. Please allow room to add later. 5-6 bullet points
qm71xrb qm71xrb
Nice first drafts everyone. I would like to see how some of these look with a white background instead of black. Nice!
I would like one design but two separate color schemes. Please match the two color schemes of the example logos provided. Thank you!

```html
<!DOCTYPE html>
<html lang="en">
<head>
<meta charset="utf-8">
<title>FixWiseDesk Business Card</title>
<link rel="stylesheet" href="https://fonts.googleapis.com/css2?family=Open+Sans:wght@400;600;700&display=swap">
<style>
  :root {
    --page-bg: #e6e7e9;
    --card-white: #ffffff;
    --card-dark: #2a2b2e;
    --card-dark-deep: #18191b;
    --brand-blue: #1f6fd6;
    --brand-blue-light: #4aa3ff;
    --steel: #9aa3ad;
    --ink-dark: #2d3440;
    --ink-light: #ffffff;
    --ink-muted: #c9ccd1;
  }
  * { margin: 0; padding: 0; box-sizing: border-box; }
  html, body { width: 1200px; height: 902px; overflow: hidden; }
  body {
    background: var(--page-bg);
    font-family: "Open Sans", Arial, sans-serif;
    display: flex;
    align-items: center;
    justify-content: center;
    gap: 40px;
  }
  .card {
    position: relative;
    width: 540px;
    height: 309px;
    border-radius: 10px;
    overflow: hidden;
    box-shadow: 0 6px 18px rgba(0,0,0,0.18);
  }
  .card--front {
    background: var(--card-white);
    display: flex;
    flex-direction: column;
    align-items: center;
    justify-content: center;
    gap: 22px;
  }
  .brand {
    display: flex;
    align-items: center;
    gap: 12px;
  }
  .brand__mark {
    width: 22px;
    height: 22px;
    background: var(--brand-blue);
  }
  .brand__name {
    font-weight: 700;
    font-size: 34px;
    color: var(--ink-dark);
    letter-spacing: 0.5px;
  }
  .card--front .website {
    font-size: 15px;
    color: var(--ink-dark);
    letter-spacing: 1px;
  }
  .card--back {
    background: linear-gradient(160deg, var(--card-dark) 0%, var(--card-dark-deep) 100%);
  }
  .card--back .brand {
    position: absolute;
    left: 34px;
    top: 52px;
  }
  .card--back .brand__name {
    color: var(--ink-light);
    font-size: 26px;
  }
  .card--back .brand__mark { width: 18px; height: 18px; background: var(--brand-blue-light); }
  .person {
    position: absolute;
    right: 34px;
    top: 40px;
    text-align: right;
  }
  .person__name {
    font-weight: 700;
    font-size: 17px;
    color: var(--ink-light);
  }
  .person__title {
    font-size: 12px;
    color: var(--ink-muted);
    margin-top: 2px;
  }
  .contact {
    position: absolute;
    right: 34px;
    top: 150px;
    list-style: none;
    text-align: right;
  }
  .contact li {
    display: flex;
    justify-content: flex-end;
    align-items: center;
    gap: 7px;
    font-size: 12px;
    color: var(--ink-light);
    line-height: 19px;
  }
  .contact svg { width: 10px; height: 10px; fill: var(--ink-light); }
  .accent-area {
    position: absolute;
    left: 0;
    bottom: 0;
    width: 540px;
    height: 78px;
    background: linear-gradient(180deg, rgba(31,111,214,0) 0%, rgba(31,111,214,0.55) 45%, rgba(154,163,173,0.45) 100%);
  }
</style>
</head>
<body>
  <section class="card card--front" aria-label="Card front">
    <div class="brand">
      <span class="brand__mark"></span>
      <span class="brand__name">FixWiseDesk</span>
    </div>
    <p class="website">www.FixWiseDesk.com</p>
  </section>

  <section class="card card--back" aria-label="Card back">
    <div class="brand">
      <span class="brand__mark"></span>
      <span class="brand__name">FixWiseDesk</span>
    </div>
    <div class="person">
      <p class="person__name">Marcus Bell</p>
      <p class="person__title">Managing Director</p>
    </div>
    <ul class="contact">
      <li>555 482 1730
        <svg viewBox="0 0 10 10" aria-hidden="true"><path d="M2 0h2l1 3-1.5 1a6 6 0 0 0 2.5 2.5L7 5l3 1v2a2 2 0 0 1-2 2A8 8 0 0 1 0 2a2 2 0 0 1 2-2z"/></svg>
      </li>
      <li>555 482 1731
        <svg viewBox="0 0 10 10" aria-hidden="true"><rect x="1" y="4" width="8" height="5"/><rect x="3" y="0" width="4" height="4"/></svg>
      </li>
      <li>service@FixWiseDesk.com
        <svg viewBox="0 0 10 10" aria-hidden="true"><path d="M0 2h10v6H0z"/></svg>
      </li>
    </ul>
    <div class="accent-area" role="img" aria-label="Decorative blue and silver wave along the bottom edge"></div>
  </section>
</body>
</html>
```